Moltbeck Chardonnay Wine Label 2024

We need a wine label design for a small, family-owned vineyard in Broke, Hunter Valley of NSW (Australia). The vineyard is called Moltbeck and we have an existing logo and 'brand book' for the vineyard home that is rented out for short stay bookings. This is attached and includes font style, colour palette and our Moltbeck logo for the accommodation (we're not wedded to this but also probably not after a completely different rethink either as we want the accommodation and the wine to feel part of the same thing.

Project:
The initial label requirement (front and back) is for the Moltbeck 2024 Chardonnay, which is called 'Juniper'. The label would need to be able to extend to other varietals (eg Verdehlo and Sparkling) in 2025. Attached is draft copy for front and back for the 2024 Chardonnay as a guide.

STYLE: We like a relatively simple, classic design and have played with both a dark (navy) and a light background (white/cream). Based on the final label design we will order a Kortap colour to pick up on the label theme.

The Chardonnay bottle dimensions are attached, as is our logo file (if that helps)

online 25-50 yearold

Wine

• front and back label design Moltbeck logo and name

```html
<!DOCTYPE html>
<html lang="en">
<head>
<meta charset="utf-8">
<title>Moltbeck Juniper Chardonnay 2024 – Front Label</title>
<link href="https://fonts.googleapis.com/css2?family=EB+Garamond:wght@400;500&family=Lato:wght@700&family=Cormorant+SC:wght@500&display=swap" rel="stylesheet">
<style>
  :root {
    --page-bg: #ebe9e4;
    --label-sage: #dae2c2;
    --navy: #434a5e;
    --ink-navy: #3e4660;
    --taupe: #9a917f;
    --wine-red: #8c1f19;
    --charcoal: #2f3136;
    --cream: #e9ecd2;
  }
  * { margin: 0; padding: 0; box-sizing: border-box; }
  html, body {
    width: 1200px;
    height: 1000px;
    overflow: hidden;
    background: var(--page-bg);
  }
  .label {
    position: absolute;
    left: 171px;
    top: 50px;
    width: 857px;
    height: 900px;
    background: var(--label-sage);
    box-shadow: 0 4px 14px rgba(0,0,0,0.18);
  }
  .brand-dot {
    position: absolute;
    left: 760px;
    top: 42px;
    width: 34px;
    height: 34px;
    border-radius: 50%;
    background: var(--ink-navy);
  }
  .brand {
    position: absolute;
    right: 84px;
    top: 96px;
    font-family: "EB Garamond", serif;
    font-weight: 500;
    font-size: 48px;
    line-height: 1;
    color: var(--ink-navy);
  }
  .range-name {
    position: absolute;
    right: 120px;
    top: 208px;
    font-family: "Lato", sans-serif;
    font-weight: 700;
    font-size: 30px;
    line-height: 1;
    letter-spacing: 0.04em;
    color: var(--taupe);
  }
  .vine-illustration {
    position: absolute;
    left: 146px;
    top: 262px;
    width: 590px;
    height: 400px;
    background: radial-gradient(ellipse at 62% 58%, rgba(62,70,96,0.30), rgba(62,70,96,0.10) 60%, rgba(62,70,96,0) 100%);
  }
  .varietal {
    position: absolute;
    left: 0;
    width: 100%;
    top: 680px;
    text-align: center;
    font-family: "EB Garamond", serif;
    font-weight: 500;
    font-size: 30px;
    letter-spacing: 0.25em;
    color: var(--wine-red);
    line-height: 1;
  }
  .vintage {
    position: absolute;
    left: 0;
    width: 100%;
    top: 719px;
    text-align: center;
    font-family: "Lato", sans-serif;
    font-weight: 700;
    font-size: 22px;
    letter-spacing: 0.06em;
    color: var(--charcoal);
    line-height: 1;
  }
  .region-band {
    position: absolute;
    left: 0;
    bottom: 0;
    width: 100%;
    height: 129px;
    background: var(--navy);
    color: var(--cream);
    text-align: center;
  }
  .region {
    position: absolute;
    left: 0;
    width: 100%;
    top: 31px;
    font-family: "Cormorant SC", serif;
    font-weight: 500;
    font-size: 32px;
    letter-spacing: 0.05em;
    line-height: 1;
  }
  .region-rule {
    position: absolute;
    left: 223px;
    top: 69px;
    width: 411px;
    height: 2px;
    background: var(--cream);
  }
  .volume {
    position: absolute;
    left: 0;
    width: 100%;
    top: 88px;
    font-family: "Cormorant SC", serif;
    font-weight: 500;
    font-size: 24px;
    letter-spacing: 0.05em;
    line-height: 1;
  }
</style>
</head>
<body>
  <main class="label">
    <span class="brand-dot"></span>
    <div class="brand">Moltbeck</div>
    <div class="range-name">JUNIPER</div>
    <div class="vine-illustration" role="img" aria-label="Engraved-style illustration of a grape cluster with vine leaves in navy ink"></div>
    <div class="varietal">CHARDONAY</div>
    <div class="vintage">2024</div>
    <footer class="region-band">
      <div class="region">Hunter Valley</div>
      <div class="region-rule"></div>
      <div class="volume">750ml</div>
    </footer>
  </main>
</body>
</html>
```